Design a Website home page for a dating / escorts website

We need home page design for dating/escorts website.
There are some specific items that we will need to be included in the design, and they are listed below. We have included some stock images that you may use in your design, and have also included the logo variations that you can use. Please feel free to use any other images that you want to, to enhance and showcase your design skills.
Please provide a Home page design for desktop view, and a separate design for mobile view. The winning design will need to be provided to us as a layered PSD that we can turn into a WordPress theme. We will need separate PSD files for desk top and mobile designs.
A full brief plus images is attached

```html
<!DOCTYPE html>
<html lang="en">
<head>
<meta charset="utf-8">
<title>Noctelle – Home</title>
<link href="https://fonts.googleapis.com/css2?family=Montserrat:wght@300;400;500;600&family=Playfair+Display:wght@700&display=swap" rel="stylesheet">
<style>
:root{
  --ink:#1f1a2d;
  --ink-deep:#17131f;
  --panel:#2a2438;
  --purple:#5a2b85;
  --red:#e5174b;
  --price:#e0245e;
  --grey:#efefef;
  --text:#3b3b3b;
  --white:#ffffff;
}
*{box-sizing:border-box;margin:0;padding:0}
html,body{width:1200px;height:3884px;overflow:hidden}
body{font-family:'Montserrat',sans-serif;color:var(--text);background:var(--white);position:relative}
h1,h2,h4{font-weight:400}
.btn{position:absolute;display:flex;align-items:center;justify-content:center;color:var(--white);font-size:11px;font-weight:500}
.btn--purple{background:var(--purple)}
.btn--red{background:var(--red)}

/* header */
.site-header{position:absolute;left:0;top:0;width:1200px;height:93px;background:var(--ink)}
.brand{position:absolute;left:526px;top:22px;width:148px;height:24px;border:1px solid #d8d4e0;color:var(--white);font-size:15px;letter-spacing:3px;font-weight:300;display:flex;align-items:center;justify-content:center}
.brand-tag{position:absolute;left:526px;top:49px;width:148px;text-align:center;font-size:5px;letter-spacing:2px;color:#aaa}
.nav{position:absolute;top:71px;left:432px;display:flex;gap:30px;font-size:8px;font-weight:600;color:var(--white)}
.nav .active{color:#8a5cc0}
.phone{position:absolute;left:866px;top:26px;color:var(--white);font-size:13px;font-style:italic;display:flex;gap:6px;align-items:center}
.book{left:865px;top:52px;width:100px;height:27px;font-size:9px}

/* photo fills: soft layered gradients in the main tones */
.ph-hero{background:
  radial-gradient(ellipse 260px 200px at 610px 150px,rgba(214,150,140,.55),transparent 70%),
  radial-gradient(ellipse 220px 260px at 140px 180px,rgba(230,120,60,.55),transparent 70%),
  radial-gradient(ellipse 200px 220px at 1080px 120px,rgba(220,150,110,.4),transparent 70%),
  radial-gradient(ellipse 300px 200px at 600px 400px,rgba(110,50,90,.7),transparent 70%),
  linear-gradient(90deg,#6a3a2e 0%,#7a4054 35%,#6e3a60 65%,#8a5a52 100%)}
.ph-welcome{background:
  radial-gradient(ellipse 260px 200px at 1000px 120px,rgba(230,210,180,.6),transparent 70%),
  radial-gradient(ellipse 300px 160px at 180px 230px,rgba(150,40,60,.7),transparent 70%),
  radial-gradient(ellipse 200px 140px at 620px 250px,rgba(60,30,40,.7),transparent 70%),
  linear-gradient(90deg,#4a1e2c,#6e2c42 40%,#7a4a4a 70%,#4a2a30)}
.ph-loc{background:
  radial-gradient(ellipse 300px 240px at 200px 120px,rgba(110,70,90,.6),transparent 70%),
  radial-gradient(ellipse 320px 260px at 1050px 300px,rgba(100,70,80,.55),transparent 70%),
  linear-gradient(135deg,#3e2c40,#2a2030 50%,#3e2c3a)}
.ph-a{background:radial-gradient(ellipse 90px 70px at 55% 18%,#d8b290,transparent 70%),radial-gradient(ellipse 120px 110px at 50% 55%,#b8907a,transparent 70%),radial-gradient(ellipse 90px 50px at 50% 70%,#2a2224,transparent 70%),linear-gradient(#7a6a62,#4a3e3a 60%,#6a5a54)}
.ph-b{background:radial-gradient(ellipse 80px 60px at 50% 20%,#d4b2a0,transparent 70%),radial-gradient(ellipse 80px 120px at 50% 60%,#f0ece8,transparent 70%),linear-gradient(#e6e2dc,#c8beb8 60%,#6a5a54)}
.ph-c{background:radial-gradient(ellipse 90px 80px at 45% 20%,#e8d2a8,transparent 70%),radial-gradient(ellipse 100px 120px at 50% 58%,#8a7e76,transparent 70%),linear-gradient(#f0eee8,#d8d2ca 60%,#b8aaa0)}
.ph-d{background:radial-gradient(ellipse 90px 120px at 50% 45%,#f0808e,transparent 70%),linear-gradient(#e0405e,#c8284a)}
.ph-e{background:radial-gradient(ellipse 80px 70px at 50% 18%,#c8a08a,transparent 70%),radial-gradient(ellipse 100px 160px at 50% 62%,#221c1e,transparent 70%),linear-gradient(#8a7e78,#5a4e4a)}
.ph-f{background:radial-gradient(ellipse 100px 80px at 50% 22%,#e8c0b0,transparent 70%),radial-gradient(ellipse 120px 90px at 55% 70%,#d8a8a0,transparent 70%),radial-gradient(ellipse 90px 200px at 30% 40%,#2a1a1e,transparent 70%),linear-gradient(#f4e0e4,#c89aa0)}
.ph-g{background:radial-gradient(ellipse 100px 90px at 50% 60%,#d0a890,transparent 70%),radial-gradient(ellipse 80px 140px at 15% 60%,#d8d4d4,transparent 70%),linear-gradient(#f0ecea,#d0cac6 50%,#8a7a74)}
.ph-h{background:radial-gradient(ellipse 90px 120px at 40% 40%,#2a1e1e,transparent 70%),radial-gradient(ellipse 120px 110px at 55% 60%,#b07a5a,transparent 70%),linear-gradient(#e8e0d8,#c8b0a0 60%,#8a6a5a)}
.ph-i{background:radial-gradient(ellipse 100px 90px at 50% 40%,#c89a80,transparent 70%),radial-gradient(ellipse 100px 60px at 55% 75%,#b0303a,transparent 70%),linear-gradient(#5a5048,#3a302c 60%,#e0dcd8)}
.ph-j{background:radial-gradient(ellipse 110px 160px at 40% 50%,#2a1c1a,transparent 70%),radial-gradient(ellipse 80px 90px at 60% 30%,#d8b8a8,transparent 70%),linear-gradient(#e8e0dc,#b8a8a0)}
.ph-k{background:radial-gradient(ellipse 80px 80px at 50% 22%,#f0e8c8,transparent 70%),radial-gradient(ellipse 110px 90px at 45% 60%,#3a3438,transparent 70%),linear-gradient(90deg,#d0c8c0,#f0ece8 50%,#a09890)}
.ph-l{background:radial-gradient(ellipse 70px 60px at 50% 18%,#c8a088,transparent 70%),radial-gradient(ellipse 90px 130px at 50% 58%,#a0283a,transparent 70%),linear-gradient(90deg,#3a2a22,#6a5248 50%,#3a2a22)}
.ph-t1{background:radial-gradient(ellipse 90px 60px at 45% 50%,#c89a80,transparent 70%),radial-gradient(ellipse 70px 60px at 60% 60%,#2a2220,transparent 70%),linear-gradient(#6a625a,#3a3230)}
.ph-t2{background:radial-gradient(ellipse 60px 70px at 55% 45%,#c8906a,transparent 70%),radial-gradient(circle at 20% 20%,rgba(240,180,100,.6),transparent 25%),linear-gradient(#7a4a30,#3a2218)}
.ph-t3{background:radial-gradient(ellipse 50px 60px at 45% 50%,#d85a3a,transparent 70%),radial-gradient(ellipse 50px 40px at 50% 25%,#8a6a5a,transparent 70%),linear-gradient(#2a2222,#141010)}
.ph-t4{background:radial-gradient(ellipse 90px 60px at 50% 40%,#e85070,transparent 70%),linear-gradient(#d8284e,#a01636)}
.ph-t5{background:radial-gradient(ellipse 80px 50px at 60% 60%,#d8a080,transparent 70%),radial-gradient(ellipse 90px 40px at 40% 85%,#f4f0ec,transparent 70%),linear-gradient(#6a8a3a,#b8a070 50%,#d8b8a0)}

/* hero */
.hero{position:absolute;left:0;top:93px;width:1200px;height:420px}
.hero h1{position:absolute;top:119px;width:100%;text-align:center;color:var(--white);font-weight:300;font-size:45px;line-height:54px}
.hero p{position:absolute;top:237px;width:100%;text-align:center;color:#eee;font-size:15px;font-weight:300}
.hero .btn{left:518px;top:280px;width:162px;height:35px}

.perks{position:absolute;left:0;top:513px;width:1200px;height:65px;background:var(--ink);color:var(--white);font-size:10px}
.perk{position:absolute;top:12px;width:200px;text-align:center}
.perk svg{display:block;margin:0 auto 6px}

/* search */
.search{position:absolute;left:234px;top:596px;width:731px;height:117px;background:var(--grey)}
.search h2{position:absolute;left:19px;top:14px;font-size:17px;color:#333}
.field{position:absolute;background:var(--white);font-size:9px;color:#bbb;display:flex;align-items:center;padding-left:12px}
.checks{position:absolute;left:12px;top:86px;display:flex;gap:20px;font-size:9px;color:#bbb}
.checks span{display:flex;align-items:center;gap:10px}
.checks i{width:11px;height:11px;background:var(--white);border:1px solid #ddd;display:inline-block}
.dropdown{position:absolute;left:658px;top:668px;width:138px;height:90px;background:var(--white);box-shadow:0 2px 6px rgba(0,0,0,.15);font-size:9px;color:#bbb}
.dropdown div{height:25px;display:flex;align-items:center;padding-left:12px}
.dropdown .hi{background:var(--red);color:var(--white)}

/* escort cards */
.card{position:absolute;top:743px;width:232px;height:356px;background:var(--grey)}
.photo{position:absolute;left:0;top:0;width:232px;height:294px}
.card .name{position:absolute;left:12px;top:304px;font-size:17px;color:#333}
.card .loc{position:absolute;left:12px;top:328px;font-size:10px;color:#aaa}
.card .price{position:absolute;right:12px;top:312px;font-size:23px;color:var(--price)}
.overlay{position:absolute;left:0;top:0;width:232px;height:294px;display:flex;align-items:center;justify-content:center;color:var(--white);font-size:15px}

/* welcome */
.welcome{position:absolute;left:0;top:1203px;width:1200px;height:281px}
.welcome h2{position:absolute;top:62px;width:100%;text-align:center;color:var(--white);font-size:21px}
.welcome .sub{position:absolute;top:96px;width:100%;text-align:center;color:var(--red);font-size:14px}
.welcome .copy{position:absolute;left:240px;top:130px;width:720px;text-align:center;color:#eee;font-size:8.5px;line-height:15px}
.welcome .btn{left:519px;top:207px;width:162px;height:35px}

.section-title{position:absolute;left:0;width:100%;text-align:center;font-size:16px;color:#333}
.tile{position:absolute;top:1567px;width:213px;height:140px;display:flex;align-items:center;justify-content:center;color:#fff;font-size:15px}

/* locations */
.locations{position:absolute;left:0;top:1752px;width:1200px;height:424px}
.locations h2{position:absolute;top:32px;width:100%;text-align:center;color:var(--white);font-size:16px}
.loc-panel{position:absolute;left:234px;top:74px;width:731px;height:312px;background:rgba(30,26,43,.88)}
.col{position:absolute;top:28px;font-size:8.5px;color:var(--white);list-style:none}
.col h4{font-size:9px;color:#aaa;margin-bottom:6px}
.col li{height:20px;display:flex;align-items:center;gap:8px}
.col b{background:var(--purple);border-radius:6px;font-size:6px;font-weight:400;padding:1px 5px}
.col h4.gap{margin-top:20px}

/* featured */
.fcard{position:absolute;width:232px;height:356px;background:var(--grey)}
.fcard .tag{position:absolute;left:12px;top:301px;font-size:8px;color:var(--red)}
.fcard .name{position:absolute;left:12px;top:313px;font-size:14px;color:#333}
.fcard .loc{position:absolute;left:12px;top:332px;font-size:8px;color:#bbb}
.fcard .from{position:absolute;right:12px;top:324px;font-size:9px;color:#333}

/* advertise */
.advertise{position:absolute;left:0;top:3423px;width:1200px;height:287px;background:var(--ink)}
.advertise h2{position:absolute;left:234px;top:22px;font-family:'Playfair Display',serif;font-weight:700;color:var(--red);font-size:20px}
.advertise .copy{position:absolute;left:234px;top:64px;width:360px;color:var(--white);font-size:11px;line-height:20px}
.advertise .btn{left:234px;top:211px;width:232px;height:35px}
.benefits{position:absolute;left:654px;top:53px;width:311px;height:200px;background:var(--panel);color:var(--white);padding:18px 0 0 18px}
.benefits h4{font-size:10px;font-weight:500;margin-bottom:6px}
.benefits ul{list-style:none}
.benefits li{font-size:8px;line-height:17.5px;padding-left:12px}

/* footer */
.site-footer{position:absolute;left:0;top:3710px;width:1200px;height:174px;background:var(--ink-deep)}
.foot-brand{position:absolute;left:234px;top:33px;display:flex;align-items:center;gap:12px;color:var(--white);font-size:18px;letter-spacing:2px}
.foot-brand i{width:68px;height:68px;border:2px solid var(--white);display:block}
.links{position:absolute;top:28px;color:var(--white)}
.links h4{font-size:10px;font-weight:500;margin-bottom:10px}
.links ul{margin-left:18px}
.links li{font-size:8px;line-height:19px}
.links li.on{color:var(--red)}
</style>
</head>
<body>

<header class="site-header">
  <div class="brand">NOCTELLE</div>
  <div class="brand-tag">VIP ESCORT AGENCY</div>
  <nav class="nav"><span>HOME</span><span>VIEW ESCORTS</span><span class="active">ADVERTISE</span><span>JOIN</span><span>ABOUT US</span></nav>
  <div class="phone"><svg width="10" height="10" viewBox="0 0 10 10"><path d="M2 0.5 L3.8 2.6 L2.8 3.8 Q4 6 6.2 7.2 L7.4 6.2 L9.5 8 L8.3 9.5 Q3 9 0.5 1.7 Z" fill="#fff"/></svg>0400 123 456</div>
  <div class="btn btn--purple book">Book an escort</div>
</header>

<section class="hero ph-hero" role="img" aria-label="Hero photograph of a glamorous model in warm evening light">
  <h1>The Best Escorts<br>of Australia</h1>
  <p>Providing our clients with discretion &amp; courtesy at all times.</p>
  <div class="btn btn--purple">See Our Escorts</div>
</section>

<section class="perks">
  <div class="perk" style="left:216px"><svg width="16" height="16"><circle cx="8" cy="8" r="6.5" fill="none" stroke="#aaa"/><circle cx="8" cy="8" r="2.5" fill="none" stroke="#aaa"/></svg>100% Real Images and Profiles</div>
  <div class="perk" style="left:408px"><svg width="16" height="16"><circle cx="8" cy="8" r="6.5" fill="none" stroke="#aaa"/><path d="M8 4v8M6 6h4M6 10h4" stroke="#aaa"/></svg>Price Match Guarantee</div>
  <div class="perk" style="left:592px"><svg width="16" height="16"><circle cx="8" cy="8" r="6.5" fill="none" stroke="#aaa"/><path d="M5 11L11 5" stroke="#aaa"/></svg>Repeat Loyalty Discounts</div>
  <div class="perk" style="left:782px"><svg width="18" height="16"><path d="M3 2h12l3 4-9 9-9-9z" fill="none" stroke="#aaa"/><path d="M0 6h18" stroke="#aaa"/></svg>High End Ladies 12-3am 7 DAYS</div>
</section>

<section class="search">
  <h2>Search Escorts by Location and Type</h2>
  <div class="field" style="left:12px;top:47px;width:395px;height:31px">Enter a location to find local escorts</div>
  <div class="field" style="left:424px;top:47px;width:138px;height:31px">All Genders</div>
  <div class="btn btn--red" style="left:581px;top:47px;width:138px;height:31px">Find Escorts</div>
  <div class="checks"><span><i></i>W4m</span><span><i></i>M4w</span><span><i></i>T4m</span><span><i></i>BDSM / Fetish</span><span><i></i>Massages</span></div>
</section>
<div class="dropdown"><div>All Genders</div><div class="hi">Female</div><div>Male</div></div>

<div class="card" style="left:-16px"><div class="photo ph-a" role="img" aria-label="Profile photo of Nina"></div><span class="name" style="left:16px">Nina</span><span class="loc" style="left:16px">Penrith</span><span class="price">$200</span></div>
<div class="card" style="left:234px"><div class="photo ph-b" role="img" aria-label="Profile photo of Britney"></div><span class="name">Britney</span><span class="loc">Central Coast</span><span class="price">$200</span></div>
<div class="card" style="left:484px"><div class="photo ph-c" role="img" aria-label="Profile photo of Erica"></div><span class="name">Erica</span><span class="loc">Rockhampton</span><span class="price">$350</span></div>
<div class="card" style="left:734px"><div class="photo ph-d" role="img" aria-label="Profile photo of Alexia"></div><div class="overlay">Passionate Redhead</div><span class="name">Alexia</span><span class="loc">Sydney</span><span class="price">$250</span></div>
<div class="card" style="left:984px"><div class="photo ph-e" role="img" aria-label="Profile photo of Heidi"></div><span class="name">Heidi</span><span class="loc">Rockingham</span><span class="price">$250</span></div>

<div class="btn btn--purple" style="left:519px;top:1128px;width:162px;height:36px">Find more escorts</div>

<section class="welcome ph-welcome" role="img" aria-label="Background photograph of a moody bedroom interior">
  <h2>Welcome to Noctelle Escorts</h2>
  <div class="sub">Premier VIP Australian Escort Agency</div>
  <p class="copy">A special welcome to the Noctelle Escort Agency. We specialise in providing clientele with Australian escorts, amazing companions capable of fulfilling your dreams and fantasies. If you are looking to set up an incall or outcall with a beautiful companion in Australia, we urge you to take a look around our site.<br>Read more...</p>
  <div class="btn btn--red">Read more</div>
</section>

<h2 class="section-title" style="top:1519px">Noctelle Categories</h2>
<div class="tile ph-t1" style="left:30px" role="img" aria-label="Category photo for women"></div>
<div class="tile ph-t2" style="left:262px" role="img" aria-label="Category photo for men"></div>
<div class="tile ph-t3" style="left:493px" role="img" aria-label="Category photo for trans"></div>
<div class="tile ph-t4" style="left:725px" role="img" aria-label="Category photo for BDSM and fetish">BDSM / Fetish</div>
<div class="tile ph-t5" style="left:956px" role="img" aria-label="Category photo for massages"></div>

<section class="locations ph-loc" role="img" aria-label="Dimmed background photograph">
  <h2>Search by Location</h2>
  <div class="loc-panel">
    <ul class="col" style="left:13px"><li><h4>QLD</h4></li>
      <li>Brisbane<b>3</b></li><li>Gold Coast<b>23</b></li><li>Sunshine Coast<b>18</b></li><li>Ipswich<b>14</b></li><li>Toowoomba<b>2</b></li><li>Bundaberg<b>25</b></li><li>Gladstone<b>6</b></li><li>Rockhampton<b>13</b></li><li>Mackay<b>24</b></li><li>Townsville<b>19</b></li><li>Cairns<b>17</b></li><li>Mount Isa<b>7</b></li></ul>
    <ul class="col" style="left:169px"><li><h4>NSW</h4></li>
      <li>Sydney<b>3</b></li><li>Kings Cross<b>23</b></li><li>North Sydney<b>18</b></li><li>Parramatta<b>14</b></li><li>Penrith<b>2</b></li><li>Newcastle<b>25</b></li><li>Wollongong<b>6</b></li><li>Central Coast<b>13</b></li><li>Coffs Harbour<b>24</b></li><li>Forster<b>19</b></li><li>Byron Bay<b>17</b></li><li>Tweed Heads<b>7</b></li></ul>
    <ul class="col" style="left:313px"><li><h4>VIC</h4></li>
      <li>Melbourne<b>3</b></li><li>St Kilda<b>23</b></li><li>Geelong<b>18</b></li><li>Ballarat<b>14</b></li>
      <li style="height:40px;align-items:flex-end"><h4>SA</h4></li><li>Adelaide<b>6</b></li><li>Glenelg<b>13</b></li><li>Flagstaff Hill<b>24</b></li></ul>
    <ul class="col" style="left:437px"><li><h4>WA</h4></li>
      <li>Perth<b>3</b></li><li>Mandurah<b>23</b></li><li>Rockingham<b>18</b></li><li>Bunbury<b>14</b></li><li>Joondalup<b>2</b></li><li>Fremantle<b>25</b></li><li>Kalgoorlie<b>6</b></li><li>Broome<b>13</b></li><li>Port Hedland<b>24</b></li></ul>
    <ul class="col" style="left:589px"><li><h4>NT</h4></li>
      <li>Darwin<b>3</b></li><li>Katherine<b>23</b></li><li>Alice Springs<b>18</b></li>
      <li style="height:40px;align-items:flex-end"><h4>ACT</h4></li><li>Canberra<b>6</b></li>
      <li style="height:40px;align-items:flex-end"><h4>TAS</h4></li><li>Hobart<b>13</b></li><li>Launceston<b>24</b></li></ul>
  </div>
</section>

<h2 class="section-title" style="top:2212px">Featured Escorts</h2>

<div class="fcard" style="left:234px;top:2262px"><div class="photo ph-f" role="img" aria-label="Featured profile photo of Alexia"></div><span class="tag">Are you ready for the Alexia Experience?</span><span class="name">Alexia</span><span class="loc">Central Coast</span><span class="from">From $400</span></div>
<div class="fcard" style="left:484px;top:2262px"><div class="photo ph-a" role="img" aria-label="Featured profile photo of Erica"></div><span class="tag">Australian "Super Lover"</span><span class="name">Erica</span><span class="loc">Sydney</span><span class="from">From $550</span></div>
<div class="fcard" style="left:734px;top:2262px"><div class="photo ph-c" role="img" aria-label="Featured profile photo of Scarlett"></div><span class="tag">High class, busty and seductive</span><span class="name">Scarlett</span><span class="loc">Melbourne</span><span class="from">From $450</span></div>

<div class="fcard" style="left:234px;top:2645px"><div class="photo ph-g" role="img" aria-label="Featured profile photo of Alexia"></div><span class="tag">Are you ready for the Alexia Experience?</span><span class="name">Alexia</span><span class="loc">Central Coast</span><span class="from">From $400</span></div>
<div class="fcard" style="left:484px;top:2645px"><div class="photo ph-h" role="img" aria-label="Featured profile photo of Erica"></div><span class="tag">Australian "Super Lover"</span><span class="name">Erica</span><span class="loc">Sydney</span><span class="from">From $550</span></div>
<div class="fcard" style="left:734px;top:2645px"><div class="photo ph-i" role="img" aria-label="Featured profile photo of Scarlett"></div><span class="tag">High class, busty and seductive</span><span class="name">Scarlett</span><span class="loc">Melbourne</span><span class="from">From $450</span></div>

<div class="fcard" style="left:234px;top:3028px"><div class="photo ph-j" role="img" aria-label="Featured profile photo of Alexia"></div><span class="tag">Are you ready for the Alexia Experience?</span><span class="name">Alexia</span><span class="loc">Central Coast</span><span class="from">From $400</span></div>
<div class="fcard" style="left:484px;top:3028px"><div class="photo ph-k" role="img" aria-label="Featured profile photo of Erica"></div><span class="tag">Australian "Super Lover"</span><span class="name">Erica</span><span class="loc">Sydney</span><span class="from">From $550</span></div>
<div class="fcard" style="left:734px;top:3028px"><div class="photo ph-l" role="img" aria-label="Featured profile photo of Scarlett"></div><span class="tag">High class, busty and seductive</span><span class="name">Scarlett</span><span class="loc">Melbourne</span><span class="from">From $450</span></div>

<section class="advertise">
  <h2>Advertise on Noctelle</h2>
  <p class="copy">Noctelle has 1000's of bookings sought every day and growing. Your success is our priority. Create your own beautiful webpage in minutes from most smart phones and PC's. Advertising is open to Independent Escorts, Body Rub, BDSM, Strip Entertainers, Agencies and Establishments. Choose from multiple advertising packages to help you increase your business.</p>
  <div class="btn btn--red">Create My Advertiser Account Now</div>
  <div class="benefits">
    <h4>Join today and receive benefits such as:</h4>
    <ul>
      <li>o Ads from $10 weekly</li>
      <li>o Easy to build and edit webpage</li>
      <li>o Friendly, helpful advertiser support</li>
      <li>o Increase your business with Featured and Standard listings</li>
      <li>o Searchable Client Safety Database</li>
      <li>o By-pass moderation option to publish yourself</li>
      <li>o "Boost to the Top" and "Available Now" options</li>
      <li>o Proudly Australian owned and operated</li>
      <li>o Safe, legal and compliant</li>
    </ul>
  </div>
</section>

<footer class="site-footer">
  <div class="foot-brand"><i></i>NOCTELLE</div>
  <div class="links" style="left:720px"><h4>QUICK LINKS</h4><ul><li>Home</li><li class="on">View Escorts</li><li>Advertise</li><li>Join</li><li>About Us</li></ul></div>
  <div class="links" style="left:884px"><h4>CATEGORIES</h4><ul><li>W4m</li><li>M4w</li><li>T4m</li><li>BDSM / Fetish</li><li>Massages</li></ul></div>
</footer>

</body>
</html>
```